Flyer-Design für die Gleichstellungsstelle einer kommunalen Stadtverwaltung
Zielgruppe
Wir sind die Gleichstellungsstelle einer kommunalen Stadtverwaltung (Einwohner*innen ca. 74.500) und richten uns mit unserer Arbeit grundsätzlich an alle Menschen. Wir möchten einen übersichtlichen Flyer haben, der die wichtigsten Rahmenbedingungen unserer Arbeit erläutert und Kontaktdaten enthält (z.B. sollen neue Mitarbeiter*innen der Verwaltung den Flyer erhalten).
Aufgabenstellung
- Der Flyer soll im Format DIN A6 sein, die Rückseite (Text) im Hochformat, die Vorderseite kann im Hoch- oder Querformat sein.
- Die Vorderseite soll gestaltet werden. Die Auswahl / Gestaltung liegt in der Kreativität der Designer*innen.
- Das Bild auf der Vorderseite kann auch eine Wortwolke kann, muss aber nicht! Begriffe für eine mögliche Wortwolke sind in an angehängten Dateien zu finden.
- Auf der Rückseite muss das angehängte Logo der Gleichstellungsstelle gemäß Corporate Design enthalten sein.
- Außer bei Fotos ist möglichst auf die Farbwelt des Corporate Designs zu achten.
- Schriftart gemäß Corporate Design (wenn möglich Avenir Next, alternativ Arial oder ähnliche Schrift).

```html
<!DOCTYPE html>
<html lang="de">
<head>
<meta charset="utf-8">
<title>Flyer Gleichstellungsstelle – Vorder- und Rückseite</title>
<link href="https://fonts.googleapis.com/css2?family=Montserrat:wght@300;400;800&family=Arimo:wght@400;700&display=swap" rel="stylesheet">
<style>
  :root{
    --bg:#2a2a2a;
    --paper:#2e2f2f;
    --paper-top:#3a3b3b;
    --white:#f2f2f2;
    --orange:#e0833a;
    --orange-text:#f0903c;
    --blue-box:#3b5bae;
    --sky:#4aa9dc;
    --teal:#3fae90;
  }
  *{margin:0;padding:0;box-sizing:border-box}
  html,body{width:1200px;height:800px;overflow:hidden;background:var(--bg)}
  .stage{position:relative;width:1200px;height:800px}
  .flyer{
    position:absolute;width:297px;height:419px;
    background:linear-gradient(180deg,var(--paper-top) 0%,var(--paper) 30%,var(--paper) 100%);
    overflow:hidden;
  }
  .flyer--front{left:274px;top:193px}
  .flyer--back{left:605px;top:180px}

  .brand{position:absolute;top:20px;right:37px;display:flex;align-items:center;gap:25px;color:var(--white);font-family:"Montserrat",sans-serif;font-weight:300}
  .brand__text{text-align:right;border-right:1px solid var(--white);padding-right:9px}
  .brand__city{font-size:8.5px;display:block}
  .brand__name{font-size:18px;display:block;line-height:1.05}
  .brand__dot{width:30px;height:30px;border-radius:50%;background:var(--orange)}

  .cloud{
    position:absolute;left:29px;top:94px;width:238px;height:238px;border-radius:50%;
    background:radial-gradient(circle at 50% 50%,
      rgba(224,131,58,.55) 0%,
      rgba(74,169,220,.40) 35%,
      rgba(63,174,144,.30) 60%,
      rgba(242,242,242,.18) 85%,
      rgba(242,242,242,0) 100%);
  }

  .slogan{position:absolute;left:0;top:361px;width:297px;height:37px;background:var(--orange);
    color:var(--white);font-family:"Montserrat",sans-serif;font-weight:800;font-size:14.5px;
    display:flex;align-items:center;justify-content:center}

  .intro{position:absolute;left:17px;top:79px;width:268px;font-family:"Arimo",sans-serif;font-size:9.6px;line-height:14px;color:var(--white)}
  .accent{color:var(--orange-text);font-weight:700}
  .tasks-title{position:absolute;left:17px;top:175px;font-family:"Arimo",sans-serif;font-weight:700;font-size:10px;color:var(--orange-text)}
  .tasks{position:absolute;left:17px;top:192px;width:270px;list-style:none;font-family:"Arimo",sans-serif;font-size:9.6px;line-height:14px;color:var(--white);hyphens:manual}
  .tasks li{position:relative;padding-left:31px;margin-bottom:6px}
  .tasks li::before{content:"";position:absolute;left:4px;top:7px;width:14px;height:14px;border-radius:50%;background:var(--sky)}

  .contact{position:absolute;left:0;top:326px;width:297px;height:72px;background:var(--orange);color:var(--white);font-family:"Arimo",sans-serif;font-weight:700;text-align:center}
  .contact__label{position:absolute;left:68px;top:-9px;width:162px;height:22px;background:var(--blue-box);font-size:9.8px;line-height:22px}
  .contact__mail{position:absolute;left:0;right:12px;top:25px;font-size:10px}
  .contact__phone{position:absolute;left:0;right:12px;top:43px;font-size:19px;letter-spacing:.5px}
</style>
</head>
<body>
<main class="stage">

  <section class="flyer flyer--front" aria-label="Vorderseite">
    <div class="brand">
      <div class="brand__text">
        <span class="brand__city">Stadt Wendenfeld</span>
        <span class="brand__name">Gleichstellungsstelle</span>
      </div>
      <span class="brand__dot"></span>
    </div>

    <div class="cloud" role="img" aria-label="Runde Wortwolke mit Begriffen zur Gleichberechtigung, umrahmt von einem kreisförmigen Schriftzug"></div>

    <div class="slogan">WIR SIND ALLE GLEICH GEBOREN!</div>
  </section>

  <section class="flyer flyer--back" aria-label="Rückseite">
    <div class="brand">
      <div class="brand__text">
        <span class="brand__city">Stadt Wendenfeld</span>
        <span class="brand__name">Gleichstellungsstelle</span>
      </div>
      <span class="brand__dot"></span>
    </div>

    <p class="intro">Die kommunale Gleichstellungsbeauftragte unterstützt die Stadtverwaltung Wendenfeld bei ihrem Auftrag, die tatsächliche Durchsetzung der <span class="accent">Gleichberechtigung</span> von Frauen und Männern zu fördern. Sie nimmt dabei alle Geschlechter in den Blick und setzt sich für den Abbau bestehender struktureller Benachteiligungen ein.</p>

    <h2 class="tasks-title">Die Gleichstellungsstelle</h2>
    <ul class="tasks">
      <li>setzt sich für die Gleichberechtigung in der Stadtver&shy;waltung und der Gesellschaft ein</li>
      <li>berät persönlich und vertraulich zu Gleichstellungs-<br>und Gleichberechtigungsfragen</li>
      <li>ist offen für Anregungen, Fragen oder Beschw&shy;erden, die Gleichstellung und Chancengleichheit betreffen</li>
    </ul>

    <div class="contact">
      <div class="contact__label">Nehmen Sie gern Kontakt auf:</div>
      <div class="contact__mail">gleichstellungsbeauftragte@wendenfeld.de</div>
      <div class="contact__phone">04871 / 23-5940</div>
    </div>
  </section>

</main>
</body>
</html>
```